Management Consulting needing a cool business card for client acquisition and networking

We are looking for a business card that is progressive and fresh that conveys innovation, forward thinking, and confidence. The business card is for a company based in Charlotte NC called, 'MERIDOX CONSULTING GROUP LLC'. The company primarily works with banks, insurance, and brokerages to implement innovative solutions to help them streamline their operations, to more effectively manage risks, and to improve their customer relationships.

Target Market(s)

Typically meet with Chief Financial Officers, Chief Information Officers, Chief Operations Officer, Business Unit Leader. The target market are generally 40-55 years, male, white, master level education plus.

Industry/Entity Type

Progressive

Font styles to use
Serif
Other font styles liked:
• Calibri

Requirements
Should not have
• Designs that look too much like law firms or accounting companies. Too conservative

```html
<!DOCTYPE html>
<html lang="en">
<head>
<meta charset="utf-8">
<title>Meridox Consulting Group LLC – Business Card</title>
<link rel="stylesheet" href="https://fonts.googleapis.com/css2?family=Lato:wght@300;400&family=Oswald:wght@500&display=swap">
<style>
  :root {
    --page-bg: #1b1b1d;
    --card-blue: #283b8e;
    --card-blue-deep: #22337c;
    --accent-red: #e33b4b;
    --ink-white: #ffffff;
    --ink-soft: #e6e9f5;
  }
  * { box-sizing: border-box; margin: 0; padding: 0; }
  html, body {
    width: 1200px; height: 926px; overflow: hidden;
    background: var(--page-bg);
  }
  .canvas {
    position: relative; width: 1200px; height: 926px;
    display: flex; flex-direction: column; align-items: center; justify-content: center; gap: 40px;
  }
  .card {
    position: relative; width: 700px; height: 400px; overflow: hidden;
    background: linear-gradient(160deg, var(--card-blue-deep), var(--card-blue));
    color: var(--ink-white);
    font-family: "Lato", sans-serif;
  }

  /* Front */
  .front .accent-band {
    position: absolute; left: 0; right: 0; bottom: 0; height: 48px;
    background: var(--accent-red);
  }
  .front .divider {
    position: absolute; left: 266px; width: 2px; background: var(--ink-white);
  }
  .divider.top { top: 0; height: 76px; }
  .divider.middle { top: 112px; height: 170px; }
  .divider.bottom { top: 304px; height: 48px; }

  .brand-mark {
    position: absolute; left: 0; top: 30px; width: 266px;
    display: flex; flex-direction: column; align-items: center; gap: 8px;
  }
  .brand-mark .dot {
    width: 56px; height: 56px; border: 1.5px solid var(--ink-white); border-radius: 50%;
  }
  .brand-mark .brand-word {
    font-size: 12px; font-weight: 400; letter-spacing: 4px;
  }

  .person {
    position: absolute; left: 0; top: 176px; width: 246px; text-align: right;
  }
  .person .name {
    font-family: "Oswald", sans-serif; font-weight: 500;
    font-size: 40px; line-height: 1; letter-spacing: 0.5px; text-transform: uppercase;
  }
  .person .role {
    margin-top: 6px; font-size: 11.5px; letter-spacing: 0.8px; text-transform: uppercase;
    color: var(--ink-soft);
  }

  .company-name {
    position: absolute; left: 296px; top: 78px;
    font-size: 30px; font-weight: 300; letter-spacing: 0.3px;
  }
  .contact {
    position: absolute; left: 296px; top: 206px;
    font-size: 16.5px; line-height: 1.5; font-style: normal; letter-spacing: 0.3px;
  }

  /* Back */
  .back {
    display: flex; flex-direction: column; align-items: center; justify-content: center; gap: 26px;
  }
  .back .dot {
    width: 170px; height: 170px; border: 1.5px solid var(--ink-white); border-radius: 50%;
  }
  .back .company-line {
    font-size: 14px; font-weight: 400; letter-spacing: 5px;
  }
</style>
</head>
<body>
  <main class="canvas">
    <section class="card back" aria-label="Card back">
      <span class="dot"></span>
      <p class="company-line">MERIDOX CONSULTING GROUP LLC</p>
    </section>

    <section class="card front" aria-label="Card front">
      <div class="brand-mark">
        <span class="dot"></span>
        <span class="brand-word">MERIDOX</span>
      </div>
      <span class="divider top"></span>
      <span class="divider middle"></span>
      <span class="divider bottom"></span>

      <div class="person">
        <p class="name">Colin R. Vane</p>
        <p class="role">Chief Solutions Architect</p>
      </div>

      <h1 class="company-name">Meridox Consulting Group LLC</h1>
      <address class="contact">
        1820 Lakeview rd., Suite 300, Charlotte, NC 28209<br>
        O: 704.555.0182 &nbsp;|&nbsp; C: 704.555.0147<br>
        e: cvane@meridoxconsulting.com
      </address>

      <div class="accent-band"></div>
    </section>
  </main>
</body>
</html>
```